Website Design for a "Talent Recruitment Agency"

We are looking for a website design for the website of our "Talent Recruitment Agency"; which is called "Crestway Hub".
Our recruitment website "Crestway Hub" will be focusing on: "Crestway Hub: Linking People & Firms in Switzerland"; which means our target audience is two-folded:
(i) TALENT - that is currently residing in- or outside of Switzerland, and is open for and interested in the "Swiss Job Market".
(ii) COMPANIES - that are looking for talent for specific job vacancies in Switzerland.
With our "Crestway Hub" approach we inted to focus on Membership & Partnership:
(a)"Membership"(TALENT)
and
(b)"Partnership"(COMPANIES)
Some of the competitor sites we like are:
• www.plimora42.dk
• www.qelvo.ch
• www.brandolix.ch/en
A sitemap example of our website is attached.
Also attached is a "Crestway Hub" logo in .eps format and one in .jpeg format.
We very much look forward to receive your creative ideas.
Best regards,
Crestway Hub
Crestway Hub: Linking People & Firms in Switzerland.
Website: crestwayhub.ch - Twitter: CrestwayHubCH
Target Market(s)
(i) TALENT (with around 0-10 years of working experience), currently residing in- or outside of Switzerland, but eligible to work in Switzerland.
(ii) COMPANIES (national or international) that are based in Switzerland.
Industry/Entity Type
Recruitment

```html
<!DOCTYPE html>
<html lang="en">
<head>
<meta charset="utf-8">
<title>Crestway Hub – About</title>
<link rel="stylesheet" href="https://fonts.googleapis.com/css2?family=Ubuntu:wght@300;400;500;700&display=swap">
<style>
:root{
  --navy-deep:#021e31;
  --navy:#06304d;
  --navy-light:#0b4a74;
  --blue-panel:#0777be;
  --orange:#f47322;
  --orange-dark:#7a2e08;
  --brand-blue:#1c7fc4;
  --ink:#10161c;
  --white:#ffffff;
  --photo-a:#8b8e92;
  --photo-b:#d9dadb;
  --social:#5a8fb8;
}
*{box-sizing:border-box;margin:0;padding:0}
html,body{width:959px;height:1200px;overflow:hidden}
body{font-family:"Ubuntu",sans-serif;background:var(--navy);color:var(--white)}
.page{position:relative;width:959px;height:1200px;overflow:hidden;
  background:linear-gradient(180deg,var(--navy) 0,var(--navy-light) 380px,var(--navy-deep) 404px,var(--navy-deep) 522px,var(--navy) 523px,var(--navy) 100%);}
.brand{position:absolute;left:38px;top:22px;display:flex;align-items:center;gap:12px}
.brand-mark{width:62px;height:62px;border-radius:50%;background:var(--brand-blue)}
.brand-name{font-size:38px;font-weight:500;color:var(--orange);line-height:1}
.brand-tagline{position:absolute;left:130px;top:82px;font-size:12.5px;font-weight:400;letter-spacing:.2px}
.languages{position:absolute;right:67px;top:56px;display:flex;gap:11px}
.languages svg{width:16px;height:11px}
.main-nav{position:absolute;right:68px;top:79px;display:flex;gap:26px;font-size:11px}
.main-nav .current{color:var(--orange)}
.hero{position:absolute;left:38px;top:133px;width:884px;height:145px;background:var(--orange);overflow:hidden}
.hero-photo{position:absolute;left:0;top:0}
.hero-title{position:absolute;left:282px;top:36px;font-size:29px;font-weight:400;color:var(--ink);line-height:1}
.hero-sub{position:absolute;left:283px;top:70px;font-size:22px;font-weight:300;color:var(--white);letter-spacing:.5px}
.content{position:absolute;left:38px;top:278px;width:884px;height:602px;background:var(--blue-panel);padding:42px 38px}
.content h1{font-size:28px;font-weight:400;margin-bottom:30px}
.content p{font-size:12.3px;font-weight:400;line-height:15.8px;text-align:justify;margin-bottom:15.8px;hyphens:auto}
.info-band{position:absolute;left:38px;top:880px;width:884px;height:243px;background:var(--orange)}
.info-col{position:absolute;top:34px;height:184px;font-size:12.5px;line-height:15.8px}
.info-col h2{font-size:17px;font-weight:400;margin-bottom:13px}
.info-col .item{margin-bottom:16px}
.info-col .more{position:absolute;bottom:0;color:var(--orange-dark);font-style:italic;font-size:12.5px}
.col-about{left:38px;width:280px}
.col-jobs{left:376px;width:215px}
.col-events{left:621px;width:230px}
.divider{position:absolute;top:38px;width:2px;height:186px;border-left:2px dotted rgba(255,255,255,.85)}
.site-footer{position:absolute;left:38px;top:1133px;font-size:10.5px;line-height:14.5px}
.social{position:absolute;left:621px;top:1131px;display:flex;gap:9px}
.social span{display:block;width:31px;height:31px;border-radius:4px;background:var(--social)}
.footer-brand{position:absolute;left:806px;top:1132px;display:flex;align-items:center;gap:6px}
.footer-brand .dot{width:30px;height:30px;border-radius:50%;background:var(--brand-blue)}
.footer-brand .name{font-size:15px;font-weight:500;color:var(--orange);line-height:1;width:80px}
</style>
</head>
<body>
<div class="page">
  <header>
    <div class="brand">
      <span class="brand-mark"></span>
      <span class="brand-name">Crestway Hub</span>
    </div>
    <div class="brand-tagline">Crestway Hub: Linking People &amp; Firms in Switzerland</div>
    <div class="languages" aria-label="Languages">
      <svg viewBox="0 0 16 11" aria-label="English"><rect width="16" height="11" fill="#1f3a8a"/><rect x="6.5" width="3" height="11" fill="#fff"/><rect y="4" width="16" height="3" fill="#fff"/><rect x="7.2" width="1.6" height="11" fill="#c8102e"/><rect y="4.7" width="16" height="1.6" fill="#c8102e"/></svg>
      <svg viewBox="0 0 16 11" aria-label="German"><rect width="16" height="3.7" fill="#111"/><rect y="3.7" width="16" height="3.6" fill="#d00"/><rect y="7.3" width="16" height="3.7" fill="#fc0"/></svg>
      <svg viewBox="0 0 16 11" aria-label="French"><rect width="5.3" height="11" fill="#23408e"/><rect x="5.3" width="5.4" height="11" fill="#fff"/><rect x="10.7" width="5.3" height="11" fill="#e1261c"/></svg>
      <svg viewBox="0 0 16 11" aria-label="Italian"><rect width="5.3" height="11" fill="#009246"/><rect x="5.3" width="5.4" height="11" fill="#fff"/><rect x="10.7" width="5.3" height="11" fill="#ce2b37"/></svg>
      <svg viewBox="0 0 16 11" aria-label="Dutch"><rect width="16" height="3.7" fill="#ae1c28"/><rect y="3.7" width="16" height="3.6" fill="#fff"/><rect y="7.3" width="16" height="3.7" fill="#21468b"/></svg>
    </div>
    <nav class="main-nav">
      <span>Home</span><span>About</span><span>Talent</span><span>Companies</span><span class="current">Jobs</span><span>Events</span><span>Contact</span>
    </nav>
  </header>

  <section class="hero">
    <svg class="hero-photo" width="240" height="145" viewBox="0 0 240 145" role="img" aria-label="Photo of four smiling business professionals standing in an office">
      <defs><linearGradient id="photoTone" x1="0" y1="0" x2="0" y2="1"><stop offset="0" stop-color="var(--photo-b)"/><stop offset="1" stop-color="var(--photo-a)"/></linearGradient></defs>
      <polygon points="0,0 240,0 218,145 0,145" fill="url(#photoTone)"/>
    </svg>
    <div class="hero-title">ABOUT</div>
    <div class="hero-sub">We are connected</div>
  </section>

  <main class="content">
    <h1>About Crestway Hub</h1>
    <p>This, of course, is not the real copy for this advertisement. The real words will be written once you have approved the headline. Rest assured, the words will expand the concept. With clarity. Conviction. And even a little wit. Because in today’s competitive marketing environment, the body copy of your advertisment must lead the reader through a series of disarmingly simple thoughts. All your supporting arguments must be communicated with simplicity and charm. And in such a way that the reader will read on. (After all, that’s a reader’s job: to read, isn’t it?) And by the time your readers have reached this point in the finished copy, you will have convinced them that you not only respect their intelligence, but you also understand their needs as consumers.</p>
    <p>As a result of which, your advertisment will repay your efforts. Take your sales; simply put, they will rise. Likewise your credibility. There’s every chance your competitors will wish they’d placed this advertisement, not you. While your customers will have probably forgotten that your competitors even exist.</p>
    <p>Which brings us, by a somewhat circuitous route, to another small point, but one which we feel should be raised. As a marketer, you probably don’t even believe in body copy. Let alone long body copy. (Unless you have a long body yourself.) Well, truth is, who’s to blame you? Fact is, too much long body copy is dotted with such indulgent little phrases like truth is, fact is, and who’s to blame you. Trust us: we guarantee, with a hand over our heart, that no such indulgent rubbish will appear in your advertisement. That’s why God gave us big blue pencils. So we can expunge every expedient example of low-witted waffle.</p>
    <p>For you, the skies will be blue, the birds will sing, and your copy will be crafted by a dedicated little man whose wife will be sitting at home, knitting, wondering why your advertisement demands more of her husband’s time than it should. But you will know why, won’t you? You will have given her husband a chance to immortalise himself in print, writing some of the most persuasive prose on behalf of a truly enlightened purveyor of widgets. And so, while your dedicated reader, enslaved to each mellifluous paragraph, clutches his newspaper with increasing interest and intention to purchase, you can count all your increased profits and take pots of money to your bank.</p>
    <p>Sadly, this is not the real copy for this advertisement. But it could well be. All you have to do is look at the account executive sitting across your desk (the fellow with the lugubrious face and the calf-like eyes), and say “Yes! Yes! Yes!” And anything you want, body copy, dinners, women, will be yours. Couldn’t be fairer than that, could we?</p>
  </main>

  <section class="info-band">
    <div class="info-col col-about">
      <h2>ABOUT</h2>
      <div class="item">Our recruitment website “Crestway Hub” will be focusing on: “Crestway Hub: Linking People &amp; Firms in Switzerland”; which means our target audience is two-folded: TALENT &amp; COMPANIES - that are looking for talent for specific job vacancies in Switzerland.</div>
      <div class="more">:: more details</div>
    </div>
    <div class="divider" style="left:335px"></div>
    <div class="info-col col-jobs">
      <h2>JOBS</h2>
      <div class="item">Trainees for Specialized Technical Trainee Program<br>09/04/2014</div>
      <div class="item">Marketing Coordinator<br>28/03/2014</div>
      <div class="more">:: more available jobs</div>
    </div>
    <div class="divider" style="left:597px"></div>
    <div class="info-col col-events">
      <h2>EVENTS</h2>
      <div class="item">Return of the mega-merger as Ravenor and Basmont turn cement into profits<br>09/04/2014</div>
      <div class="item">Swiss startups get help with US market breakthrough<br>28/03/2014</div>
      <div class="more">:: more events</div>
    </div>
  </section>

  <footer>
    <div class="site-footer">Copyright 2014 crestwayhub.ch. All Rights Reserved.<br>Terms &amp; Conditions | Disclaimer</div>
    <div class="social" aria-label="Social networks"><span></span><span></span><span></span><span></span></div>
    <div class="footer-brand"><span class="dot"></span><span class="name">Crestway Hub</span></div>
  </footer>
</div>
</body>
</html>
```